Print on top the name of the company: (Or Similar)
Larkmoor Cleaning & Disinfecting
Because your standards aren't standard.

We adhere to ALL NVB guidelines for both residential and commercial cleaning.

Infection Control is our ultimate goal.

Instructions:
Opening a residential and commercial cleaning and disinfecting company in south Florida.

Targeting high-end residential clients, commercial and healthcare facilities, specializing in Ambulatory Care Guidelines. With a concentration and expertise in targeting Covid 19 and other transmissible pathogens.

UMRE trained.
Owned and operated by a licensed BSN Registered Nurse specially ​trained in Infection Control Prevention with over 25 years experience. Over two decades in Ambulatory Surgery Center Administration, Director of Nursing and Infection Control Prevention ad Consulting.

Looking to create a business flier that emphasizes Cleaning & Disinfection
along with the standard expectation for residential and Commercial cleaning services
Updates

Need extra days to review

Target Market(s)

Residential & Commercial

Font styles to use
Decorative

Requirements
Must have
• A checklist for cleaning services

```html
<!DOCTYPE html>
<html lang="en">
<head>
<meta charset="utf-8">
<title>Larkmoor Cleaning &amp; Disinfecting – Flyer</title>
<link rel="stylesheet" href="https://fonts.googleapis.com/css2?family=Montserrat:wght@600;700;800;900&family=Open+Sans:wght@400;600&display=swap">
<style>
  :root{
    --navy:#1f1f5c;
    --navy-deep:#16164a;
    --plum:#5a2a6e;
    --red:#e0262c;
    --white:#ffffff;
    --paper:#ffffff;
    --ink:#333344;
    --muted:#5a5a6e;
    --rule:#d6d6e0;
    --info-bg:#f4f4f8;
    --photo-a:#c9ccd6;
    --photo-b:#8f93a8;
  }
  *{box-sizing:border-box;margin:0;padding:0}
  html,body{width:738px;height:1200px;overflow:hidden;background:var(--paper)}
  body{font-family:"Open Sans",Arial,sans-serif;color:var(--ink)}
  .flyer{position:relative;width:738px;height:1200px;background:var(--paper);overflow:hidden}

  /* Header */
  .header{position:absolute;left:0;top:0;width:738px;height:320px;
    background:linear-gradient(100deg,var(--navy-deep) 0%,var(--navy) 45%,var(--plum) 100%)}
  .header-photo{position:absolute;right:0;top:0;width:330px;height:320px;
    background:linear-gradient(180deg,#8a6f93 0%,#c7b9cc 55%,#e8e2ea 100%)}
  .header-photo::before{content:"";position:absolute;inset:0;
    background:linear-gradient(90deg,var(--navy) 0%,rgba(31,31,92,0) 40%)}
  .brand{position:absolute;left:38px;top:38px;width:420px}
  .brand-name{font-family:"Montserrat",Arial,sans-serif;font-weight:900;color:var(--white);
    font-size:34px;line-height:1.08;text-transform:uppercase;letter-spacing:.3px}
  .goal{margin-top:14px;font-family:"Montserrat",Arial,sans-serif;font-weight:900;color:var(--red);
    font-size:28px;line-height:1.08;text-transform:uppercase}
  .adhere{margin-top:16px;color:var(--white);font-size:14px;line-height:1.45;font-weight:600;width:360px}

  /* Info section */
  .info{position:absolute;left:0;top:320px;width:738px;height:240px;background:var(--info-bg);
    display:flex;padding:24px 38px 0}
  .info-col{flex:1 1 0;min-width:0}
  .info-col + .info-col{margin-left:38px}
  .info-title{font-family:"Montserrat",Arial,sans-serif;font-weight:800;font-size:18px;color:var(--navy);
    text-transform:uppercase;padding-bottom:8px;border-bottom:2px solid var(--rule);margin-bottom:12px}
  .info-text{font-size:11.5px;line-height:1.55;color:var(--muted);margin-bottom:8px}

  /* Services */
  .services{position:absolute;left:0;top:530px;width:738px;height:610px;background:var(--navy);
    border-radius:40px 40px 0 0;padding:30px 38px 0}
  .service-cols{display:flex;height:100%}
  .service-col{flex:1 1 0;min-width:0;display:flex;flex-direction:column}
  .service-col + .service-col{margin-left:38px}
  .service-title{font-family:"Montserrat",Arial,sans-serif;font-weight:900;font-size:28px;
    color:var(--red);text-transform:uppercase;text-align:center;margin-bottom:12px}
  .checklist{list-style:none;margin:0 auto;width:100%;max-width:260px}
  .checklist li{display:flex;align-items:center;gap:10px;color:var(--white);white-space:nowrap;
    font-family:"Montserrat",Arial,sans-serif;font-weight:600;font-size:15px;line-height:1.85}
  .checklist svg{flex:none}
  .photo-card{margin-top:auto;margin-bottom:24px;height:170px;background:var(--white);
    border-radius:26px;display:flex;align-items:center;justify-content:center;gap:4px;padding:0 8px}
  .photo-circle{flex:none;border-radius:50%;border:4px solid var(--navy);
    background:radial-gradient(circle at 40% 35%,var(--photo-a),var(--photo-b))}
  .photo-circle.small{width:84px;height:84px}
  .photo-circle.large{width:116px;height:116px}

  /* Call bar */
  .call-bar{position:absolute;left:0;bottom:0;width:738px;height:60px;background:var(--red);
    display:flex;align-items:center;justify-content:center;color:var(--white);
    font-family:"Montserrat",Arial,sans-serif;font-weight:800;font-size:22px;letter-spacing:1px;text-transform:uppercase}
</style>
</head>
<body>
<main class="flyer">
  <header class="header">
    <div class="header-photo" role="img" aria-label="Photo of a smiling cleaner in a green apron and yellow gloves"></div>
    <div class="brand">
      <h1 class="brand-name">Larkmoor Cleaning &amp; Disinfecting</h1>
      <p class="goal">Infection control is our ultimate goal</p>
      <p class="adhere">We adhere to ALL NVB guidelines for both residential and commercial cleaning.</p>
    </div>
  </header>

  <section class="info">
    <div class="info-col">
      <h2 class="info-title">Instructions:</h2>
      <p class="info-text">Opening a residential and commercial cleaning and disinfecting company in south Florida.</p>
      <p class="info-text">Targeting high-end residential clients, commercial and healthcare facilities, specializing in Ambulatory Care Guidelines, with expertise in Covid 19 and other transmissible pathogens.</p>
    </div>
    <div class="info-col">
      <h2 class="info-title">UMRE Trained</h2>
      <p class="info-text">Owned and operated by a licensed BSN Registered Nurse specially trained in Infection Control Prevention with over 25 years experience.</p>
      <p class="info-text">Over two decades in Ambulatory Surgery Center Administration, Director of Nursing and Infection Control Prevention and Consulting.</p>
    </div>
  </section>

  <section class="services">
    <div class="service-cols">
      <div class="service-col">
        <h2 class="service-title">Commercial</h2>
        <ul class="checklist">
          <li><svg width="14" height="14" viewBox="0 0 14 14"><path d="M2 7.5l3 3 7-7" fill="none" stroke="#e0262c" stroke-width="2.4" stroke-linecap="round" stroke-linejoin="round"/></svg>Janitorial</li>
          <li><svg width="14" height="14" viewBox="0 0 14 14"><path d="M2 7.5l3 3 7-7" fill="none" stroke="#e0262c" stroke-width="2.4" stroke-linecap="round" stroke-linejoin="round"/></svg>Offices</li>
          <li><svg width="14" height="14" viewBox="0 0 14 14"><path d="M2 7.5l3 3 7-7" fill="none" stroke="#e0262c" stroke-width="2.4" stroke-linecap="round" stroke-linejoin="round"/></svg>Floor Maintenance</li>
          <li><svg width="14" height="14" viewBox="0 0 14 14"><path d="M2 7.5l3 3 7-7" fill="none" stroke="#e0262c" stroke-width="2.4" stroke-linecap="round" stroke-linejoin="round"/></svg>Carpet Cleaning</li>
          <li><svg width="14" height="14" viewBox="0 0 14 14"><path d="M2 7.5l3 3 7-7" fill="none" stroke="#e0262c" stroke-width="2.4" stroke-linecap="round" stroke-linejoin="round"/></svg>Move - Ins</li>
          <li><svg width="14" height="14" viewBox="0 0 14 14"><path d="M2 7.5l3 3 7-7" fill="none" stroke="#e0262c" stroke-width="2.4" stroke-linecap="round" stroke-linejoin="round"/></svg>Move - Outs</li>
          <li><svg width="14" height="14" viewBox="0 0 14 14"><path d="M2 7.5l3 3 7-7" fill="none" stroke="#e0262c" stroke-width="2.4" stroke-linecap="round" stroke-linejoin="round"/></svg>Constructions Clean - Ups</li>
          <li><svg width="14" height="14" viewBox="0 0 14 14"><path d="M2 7.5l3 3 7-7" fill="none" stroke="#e0262c" stroke-width="2.4" stroke-linecap="round" stroke-linejoin="round"/></svg>Estate Clean - Outs</li>
        </ul>
        <div class="photo-card">
          <div class="photo-circle small" role="img" aria-label="Photo of an office floor being cleaned"></div>
          <div class="photo-circle large" role="img" aria-label="Photo of a cleaner disinfecting a commercial space"></div>
          <div class="photo-circle small" role="img" aria-label="Photo of a vacuum on office carpet"></div>
        </div>
      </div>
      <div class="service-col">
        <h2 class="service-title">Residential</h2>
        <ul class="checklist">
          <li><svg width="14" height="14" viewBox="0 0 14 14"><path d="M2 7.5l3 3 7-7" fill="none" stroke="#e0262c" stroke-width="2.4" stroke-linecap="round" stroke-linejoin="round"/></svg>House Cleaning</li>
          <li><svg width="14" height="14" viewBox="0 0 14 14"><path d="M2 7.5l3 3 7-7" fill="none" stroke="#e0262c" stroke-width="2.4" stroke-linecap="round" stroke-linejoin="round"/></svg>Before And After Party</li>
          <li><svg width="14" height="14" viewBox="0 0 14 14"><path d="M2 7.5l3 3 7-7" fill="none" stroke="#e0262c" stroke-width="2.4" stroke-linecap="round" stroke-linejoin="round"/></svg>Move - Ins</li>
          <li><svg width="14" height="14" viewBox="0 0 14 14"><path d="M2 7.5l3 3 7-7" fill="none" stroke="#e0262c" stroke-width="2.4" stroke-linecap="round" stroke-linejoin="round"/></svg>Move - Outs</li>
          <li><svg width="14" height="14" viewBox="0 0 14 14"><path d="M2 7.5l3 3 7-7" fill="none" stroke="#e0262c" stroke-width="2.4" stroke-linecap="round" stroke-linejoin="round"/></svg>Holiday Cleaning</li>
          <li><svg width="14" height="14" viewBox="0 0 14 14"><path d="M2 7.5l3 3 7-7" fill="none" stroke="#e0262c" stroke-width="2.4" stroke-linecap="round" stroke-linejoin="round"/></svg>Seasonal Cleaning</li>
          <li><svg width="14" height="14" viewBox="0 0 14 14"><path d="M2 7.5l3 3 7-7" fill="none" stroke="#e0262c" stroke-width="2.4" stroke-linecap="round" stroke-linejoin="round"/></svg>Carpet Cleaning</li>
          <li><svg width="14" height="14" viewBox="0 0 14 14"><path d="M2 7.5l3 3 7-7" fill="none" stroke="#e0262c" stroke-width="2.4" stroke-linecap="round" stroke-linejoin="round"/></svg>Deodorizing And Sanitizing</li>
        </ul>
        <div class="photo-card">
          <div class="photo-circle small" role="img" aria-label="Photo of a tidy living room"></div>
          <div class="photo-circle large" role="img" aria-label="Photo of a cleaner wiping a kitchen counter"></div>
          <div class="photo-circle small" role="img" aria-label="Photo of cleaning supplies in a bathroom"></div>
        </div>
      </div>
    </div>
  </section>

  <footer class="call-bar">Please call us at (555) 014 27 93</footer>
</main>
</body>
</html>
```